Banner Ad Design Project

We I need three call to action buttons for my new web site. The site is a medical supply company. that should equal 1030x280. The site buttons should say:

1- "EVERYDAY FREE SHIPPING on orders over $50. No code. No hassle."
2- "Call us for FREE EXPERT ADVICE. Click to learn more."
3- "Learn about our QLT Program. Click to continue"

The site is brontawick.com, I need them to replace the flash banner on the home page. I have proper placement, but need them to be distinct colors so they get noticed.

Thank you!

```html
<!DOCTYPE html>
<html lang="en">
<head>
<meta charset="utf-8">
<title>Everyday Free Shipping</title>
<link rel="stylesheet" href="https://fonts.googleapis.com/css2?family=Arimo:wght@700&family=Archivo+Black&display=swap">
<style>
  :root {
    --canvas-bg: #ffffff;
    --frame-blue: #2f7fc1;
    --panel-green: #9dd3a0;
    --headline-blue: #2a7ec6;
    --body-black: #111111;
    --button-top: #8fe08a;
    --button-mid: #4cbf4a;
    --button-bottom: #2e9a31;
    --button-edge: #1f6e22;
    --truck-red: #c8231f;
    --truck-dark: #7a1212;
  }
  * { margin: 0; padding: 0; box-sizing: border-box; }
  html, body {
    width: 1200px;
    height: 326px;
    overflow: hidden;
    background: var(--canvas-bg);
  }
  .banner {
    position: relative;
    width: 1200px;
    height: 326px;
    background: var(--canvas-bg);
    border: 3px solid var(--frame-blue);
  }
  .offer-panel {
    position: absolute;
    left: 10px;
    top: 46px;
    width: 842px;
    height: 126px;
    background: var(--panel-green);
    border-radius: 10px;
  }
  .offer-title {
    position: absolute;
    left: 18px;
    top: 8px;
    font-family: "Arimo", Arial, sans-serif;
    font-weight: 700;
    font-size: 59px;
    line-height: 1;
    letter-spacing: -0.5px;
    color: var(--headline-blue);
    white-space: nowrap;
    text-shadow: 1px 1px 0 rgba(0,0,0,0.15);
  }
  .offer-terms {
    position: absolute;
    left: 18px;
    top: 76px;
    font-family: "Archivo Black", "Arial Black", sans-serif;
    font-size: 30px;
    line-height: 1;
    color: var(--body-black);
    white-space: nowrap;
  }
  .cta-button {
    position: absolute;
    left: 24px;
    top: 201px;
    width: 314px;
    height: 59px;
    border-radius: 10px;
    background: linear-gradient(to bottom, var(--button-top) 0%, var(--button-mid) 55%, var(--button-bottom) 100%);
    border: 2px solid var(--button-edge);
    box-shadow: 3px 4px 4px rgba(0,0,0,0.45);
    display: flex;
    align-items: center;
    justify-content: center;
    font-family: "Arimo", Arial, sans-serif;
    font-weight: 700;
    font-size: 32px;
    color: var(--body-black);
    text-decoration: none;
  }
  .delivery-illustration {
    position: absolute;
    left: 852px;
    top: 16px;
    width: 344px;
    height: 278px;
    border-radius: 18px;
    background: radial-gradient(ellipse at 45% 45%, var(--truck-red) 0%, #b01e1a 45%, rgba(200,35,31,0.25) 75%, rgba(255,255,255,0) 100%);
  }
</style>
</head>
<body>
  <div class="banner">
    <div class="offer-panel">
      <div class="offer-title">EVERYDAY FREE SHIPPING</div>
      <div class="offer-terms">on orders over $50. No code. No hassle !</div>
    </div>
    <a class="cta-button" href="#">Know More</a>
    <div class="delivery-illustration" role="img" aria-label="Red delivery van loaded with cardboard boxes and a hand truck, marked Free Shipping"></div>
  </div>
</body>
</html>
```